New corporate stationery design for UK train leasing company

In advance of an office move later this year we are looking to redesign all our corporate stationery (business cards, letterhead, compliment slips, envelopes etc) as well as small branded items (such as mouse mats, drink mats, etc).

We wish to keep the same logo and corporate colours but are looking for a modern, fresh look that will tie in our stationery more with the look of our website and our PowerPoint template. We have a strapline, "Track Crews, True Knowhow" that we would like to incorporate into the stationery design and also need to include a "TEMLO" logo on the bottom of the letterhead/compliment slips. We have two offices so will need letterhead and compliment slips with both addresses.

The files attached include different versions of our logo (the main one is the black with green halo, file 1 or 3), our brand guidelines summary (including Pantone colours), the TEMLO logo and PowerPoint template.

More information about the business can be found at www.fernholtrail.co.uk.

If you have any questions please let me know.

I look forward to seeing the designs!
Regards
Moira

Target Market(s)

Main audience are train operators, rail industry suppliers, passenger transport groups, government and other political organisations, financiers/lenders.

Industry/Entity Type

Business

```html
<!DOCTYPE html>
<html lang="en">
<head>
<meta charset="utf-8">
<title>Fernhol Rail Stationery</title>
<link rel="stylesheet" href="https://fonts.googleapis.com/css2?family=Open+Sans:wght@400;600;700&display=swap">
<style>
  :root {
    --teal: #17a88f;
    --teal-dark: #12937d;
    --paper: #ffffff;
    --backdrop: #c4c4c4;
    --ink: #1d2a4a;
    --soft: #e8f6f3;
  }
  * { box-sizing: border-box; margin: 0; padding: 0; }
  html, body { width: 900px; height: 1200px; overflow: hidden; }
  body {
    background: var(--backdrop);
    font-family: "Open Sans", Arial, sans-serif;
    position: relative;
  }
  .sheet { position: absolute; }
  .brand { color: var(--paper); line-height: 1; }
  .brand-name { font-weight: 600; letter-spacing: -0.5px; }
  .brand-line { font-weight: 400; margin-top: 4px; }

  /* Letterhead */
  .letterhead { left: 24px; top: 15px; width: 420px; height: 624px; background: var(--paper); }
  .letterhead-band { position: absolute; left: 0; top: 0; width: 100%; height: 174px; background: var(--teal); }
  .letterhead .brand { position: absolute; left: 18px; top: 50px; }
  .letterhead .brand-name { font-size: 36px; }
  .letterhead .brand-line { font-size: 9px; }
  .contact { position: absolute; color: var(--paper); font-size: 6.5px; line-height: 1.45; }
  .letterhead .contact { left: 252px; top: 22px; }
  .contact strong { font-weight: 700; }
  .registration { position: absolute; left: 0; top: 182px; width: 100%; text-align: center; font-size: 5.5px; color: var(--teal-dark); }
  .web { position: absolute; left: 0; bottom: 16px; width: 100%; text-align: center; font-size: 5.5px; color: #555; }
  .partner { position: absolute; font-weight: 700; color: var(--ink); letter-spacing: 0.5px; }
  .letterhead .partner { right: 16px; bottom: 30px; font-size: 16px; }
  .edge-mark { position: absolute; left: 0; bottom: 24px; width: 5px; height: 40px; background: var(--teal); }

  /* Folder */
  .folder { left: 459px; top: 15px; width: 420px; height: 624px; background: var(--teal); }
  .folder .brand { position: absolute; left: 0; top: 276px; width: 100%; text-align: center; }
  .folder .brand-name { font-size: 40px; }
  .folder .brand-line { font-size: 9px; }

  /* Business cards */
  .card { top: 684px; width: 180px; height: 102px; }
  .card-front { left: 30px; background: var(--paper); }
  .card-front-band { position: absolute; left: 0; top: 18px; width: 82px; height: 44px; background: var(--teal); }
  .card-front .brand { position: absolute; left: 8px; top: 26px; }
  .card-front .brand-name { font-size: 15px; }
  .card-front .brand-line { font-size: 4.5px; margin-top: 2px; }
  .card-front .person { position: absolute; left: 96px; top: 22px; font-size: 5px; line-height: 1.5; color: #333; }
  .person strong { color: var(--teal-dark); font-weight: 700; }
  .card-back { left: 225px; background: var(--teal); }
  .card-back .brand { position: absolute; left: 10px; top: 28px; }
  .card-back .brand-name { font-size: 15px; }
  .card-back .brand-line { font-size: 4.5px; margin-top: 2px; }
  .card-back .person { position: absolute; left: 106px; top: 12px; font-size: 5px; line-height: 1.5; color: var(--paper); }
  .card-back .person strong { color: var(--paper); }

  /* Envelopes */
  .envelope-back { left: 30px; top: 810px; width: 330px; height: 180px; }
  .envelope-front { left: 150px; top: 900px; width: 480px; height: 285px; background: var(--teal); box-shadow: 0 2px 6px rgba(0,0,0,0.15); }
  .envelope-front .brand { position: absolute; left: 24px; top: 22px; }
  .envelope-front .brand-name { font-size: 30px; }
  .envelope-front .brand-line { font-size: 7px; }
  .envelope-front .rule { position: absolute; left: 0; top: 118px; width: 100%; height: 1px; background: rgba(255,255,255,0.4); }
  .envelope-front .contact { left: 24px; top: 210px; font-size: 6.5px; }
  .envelope-front .partner { right: 16px; bottom: 16px; font-size: 16px; }
</style>
</head>
<body>

  <section class="sheet letterhead" aria-label="Letterhead">
    <div class="letterhead-band"></div>
    <div class="brand">
      <div class="brand-name">fernhol</div>
      <div class="brand-line">Track Crews, True Knowhow</div>
    </div>
    <div class="contact">
      <strong>Head Office</strong><br>
      14 Carden Row, Leeds LS1 4QT<br>
      T: 0113 496 0521<br>
      E: info@fernholtrail.co.uk
    </div>
    <p class="registration">Registered in England No. 0481 2276 &nbsp; 2 Wharf Lane, London SE1 9PL</p>
    <span class="edge-mark"></span>
    <div class="partner">TEMLO</div>
    <p class="web">www.fernholtrail.co.uk</p>
  </section>

  <section class="sheet folder" aria-label="Presentation folder">
    <div class="brand">
      <div class="brand-name">fernhol</div>
      <div class="brand-line">Track Crews, True Knowhow</div>
    </div>
  </section>

  <section class="sheet card card-front" aria-label="Business card front">
    <div class="card-front-band"></div>
    <div class="brand">
      <div class="brand-name">fernhol</div>
      <div class="brand-line">Track Crews, True Knowhow</div>
    </div>
    <div class="person">
      <strong>Moira Hale</strong><br>
      Office Manager<br>
      T: 0113 496 0521<br>
      moira@fernholtrail.co.uk
    </div>
  </section>

  <section class="sheet card card-back" aria-label="Business card back">
    <div class="brand">
      <div class="brand-name">fernhol</div>
      <div class="brand-line">Track Crews, True Knowhow</div>
    </div>
    <div class="person"><strong>Moira Hale</strong></div>
  </section>

  <svg class="sheet envelope-back" viewBox="0 0 330 180" aria-label="Envelope back">
    <rect width="330" height="180" fill="var(--teal)"/>
    <polygon points="0,0 330,0 330,24 165,74 0,24" fill="var(--paper)"/>
  </svg>

  <section class="sheet envelope-front" aria-label="Envelope front">
    <div class="brand">
      <div class="brand-name">fernhol</div>
      <div class="brand-line">Track Crews, True Knowhow</div>
    </div>
    <div class="rule"></div>
    <div class="contact">
      <strong>Head Office</strong><br>
      14 Carden Row<br>
      Leeds LS1 4QT<br>
      www.fernholtrail.co.uk
    </div>
    <div class="partner">TEMLO</div>
  </section>

</body>
</html>
```